Business card for plumber

I need a business card for my plumbing company.
on it should:
Surname
position
E-mail
Telephone & mobile phone
Website
Please everything as placeholders / fantasy names.
We stand for high quality, hygiene and professionalism.

Colours:
# 606060 anthracite
# f7931e orange
# 2b89cc blue

Industry/Entity Type

Plumber

Contact Information for Business Card

folgt...

```html
<!DOCTYPE html>
<html lang="de">
<head>
<meta charset="utf-8">
<title>Kessler Sanitär – Visitenkarte</title>
<link href="https://fonts.googleapis.com/css2?family=Arimo:wght@400;700&display=swap" rel="stylesheet">
<style>
  :root {
    --anthracite: #333333;
    --grey-text: #4a4a4a;
    --orange: #f7931e;
    --blue: #1f6fb8;
    --card: #efefef;
    --backdrop: #e4e2de;
  }
  * { margin: 0; padding: 0; box-sizing: border-box; }
  html, body { width: 1200px; height: 800px; overflow: hidden; }
  body {
    background: var(--backdrop);
    font-family: "Arimo", Arial, sans-serif;
    position: relative;
  }
  .card {
    position: absolute;
    top: 245px;
    width: 540px;
    height: 309px;
    background: var(--card);
    box-shadow: 0 6px 18px rgba(0,0,0,0.12);
  }
  .card--front { left: 40px; }
  .card--back { left: 620px; }

  .brand {
    display: flex;
    align-items: center;
  }
  .brand__square {
    display: inline-block;
    background: var(--orange);
    flex: none;
  }
  .brand__name {
    color: var(--blue);
    font-weight: 700;
    line-height: 1;
    white-space: nowrap;
  }

  /* front */
  .front-brand {
    position: absolute;
    right: 20px;
    bottom: 56px;
    gap: 12px;
  }
  .front-brand .brand__square { width: 22px; height: 22px; }
  .front-brand .brand__name { font-size: 30px; }
  .front-web {
    position: absolute;
    right: 20px;
    bottom: 26px;
    font-size: 12px;
    letter-spacing: 0.6px;
    color: var(--blue);
  }

  /* back */
  .back-brand {
    position: absolute;
    left: 30px;
    top: 72px;
    gap: 10px;
  }
  .back-brand .brand__square { width: 16px; height: 16px; }
  .back-brand .brand__name { font-size: 22px; }
  .person {
    position: absolute;
    right: 20px;
    top: 68px;
    text-align: right;
  }
  .person__name {
    font-size: 19px;
    font-weight: 700;
    letter-spacing: 0.6px;
    color: var(--anthracite);
  }
  .person__role {
    font-size: 14px;
    color: var(--grey-text);
    margin-top: 4px;
  }
  .contact {
    position: absolute;
    left: 30px;
    bottom: 22px;
    list-style: none;
    font-size: 13px;
    line-height: 19px;
    color: var(--anthracite);
    letter-spacing: 0.3px;
  }
</style>
</head>
<body>
  <section class="card card--front">
    <div class="brand front-brand">
      <span class="brand__square"></span>
      <span class="brand__name">KESSLER SANITÄR</span>
    </div>
    <div class="front-web">www.kessler-sanitaer.de</div>
  </section>

  <section class="card card--back">
    <div class="brand back-brand">
      <span class="brand__square"></span>
      <span class="brand__name">KESSLER SANITÄR</span>
    </div>
    <div class="person">
      <div class="person__name">LUKAS BERGER</div>
      <div class="person__role">Managing Director</div>
    </div>
    <ul class="contact">
      <li>Tel. 0421 987 6543</li>
      <li>Mobil 0171 246 8135</li>
      <li>kontakt@kessler-sanitaer.de</li>
      <li>www.kessler-sanitaer.de</li>
    </ul>
  </section>
</body>
</html>
```